BKA

Please send us some options for letterhead I attached our Logo. In addition to the Logo we need this information somewhere on the page

47 Fenbury Lane
Ashbrook, CT 06412
203-481-7629

```html
<!DOCTYPE html>
<html lang="en">
<head>
<meta charset="utf-8">
<title>BKA Letterhead</title>
<link rel="stylesheet" href="https://fonts.googleapis.com/css2?family=Arimo:wght@400;700&display=swap">
<style>
  :root {
    --paper: #ffffff;
    --sky-deep: #b6c4e6;
    --sky-light: #e2eaf6;
    --brand-brown: #4b423e;
    --footer-text: #ffffff;
  }
  * { margin: 0; padding: 0; box-sizing: border-box; }
  html, body {
    width: 881px;
    height: 1200px;
    overflow: hidden;
    background: var(--paper);
  }
  .letterhead {
    position: relative;
    width: 881px;
    height: 1200px;
    background: var(--paper);
    font-family: "Arimo", Arial, sans-serif;
  }
  .header-band {
    position: absolute;
    top: 0;
    height: 138px;
  }
  .header-band--left {
    left: 0;
    width: 314px;
    background: linear-gradient(90deg, var(--sky-deep), var(--sky-light));
  }
  .header-band--right {
    right: 0;
    width: 312px;
    background: linear-gradient(90deg, var(--sky-light), var(--sky-deep));
  }
  .brand {
    position: absolute;
    top: 152px;
    left: 0;
    width: 881px;
    display: flex;
    justify-content: center;
    align-items: center;
    gap: 10px;
  }
  .brand__mark {
    width: 14px;
    height: 14px;
    background: var(--brand-brown);
  }
  .brand__name {
    font-weight: 700;
    font-size: 52px;
    letter-spacing: 3px;
    line-height: 1;
    color: var(--brand-brown);
  }
  .footer-band {
    position: absolute;
    left: 0;
    top: 1158px;
    width: 881px;
    height: 24px;
    background: var(--brand-brown);
    display: flex;
    justify-content: center;
    align-items: center;
    gap: 8px;
    color: var(--footer-text);
    font-size: 13.5px;
    letter-spacing: 0.2px;
    white-space: nowrap;
  }
  .footer-band__phone {
    display: inline-flex;
    align-items: center;
    gap: 5px;
    margin-left: 6px;
  }
  .footer-band__icon {
    width: 15px;
    height: 15px;
  }
</style>
</head>
<body>
  <main class="letterhead">
    <div class="header-band header-band--left" role="img" aria-label="Light blue sunburst header decoration"></div>
    <div class="header-band header-band--right" role="img" aria-label="Light blue sunburst header decoration"></div>

    <div class="brand">
      <span class="brand__mark"></span>
      <span class="brand__name">BKA</span>
    </div>

    <footer class="footer-band">
      <span class="footer-band__address">47 FENBURY LANE, ASHBROOK, CT 06412</span>
      <span class="footer-band__phone">
        <svg class="footer-band__icon" viewBox="0 0 16 16" aria-hidden="true">
          <circle cx="8" cy="8" r="7" fill="none" stroke="#ffffff" stroke-width="1.1"/>
          <path d="M6 4.2c-.9.4-1.4 1.3-1.1 2.6.4 1.8 1.9 3.9 3.5 4.8 1.1.6 2 .5 2.6-.2l-1.4-1.6-.9.4c-.8-.5-1.6-1.7-1.8-2.6l.8-.6z" fill="#ffffff"/>
        </svg>
        203-481-7629
      </span>
    </footer>
  </main>
</body>
</html>
```